Velno Recycling needs a new web design

We need a new web design for our company based in Austin, TX. We resell and recycling electronics such as laptops, computer components, Tovlets, Brunos, etc. Since our inception over ten years ago, we’ve become one of the premier electronics recycling and remarketing companies in Austin, Texas.

```html
<!DOCTYPE html>
<html lang="en">
<head>
<meta charset="utf-8">
<title>Velno Recycling</title>
<link href="https://fonts.googleapis.com/css2?family=Poppins:wght@300;400;500;600;700&display=swap" rel="stylesheet">
<style>
:root{
  --green-dark:#1f6a2a;
  --green:#3f9a35;
  --green-light:#7cc24a;
  --blue:#1ba1e2;
  --navy:#0f3f8c;
  --ink:#222a33;
  --text:#5d6670;
  --grey-band:#d9dee4;
  --grey-soft:#ececec;
  --footer:#7a7a7a;
  --white:#ffffff;
}
*{box-sizing:border-box;margin:0;padding:0}
html,body{width:1200px;height:3315px;overflow:hidden}
body{font-family:'Poppins',sans-serif;color:var(--text);background:var(--white);position:relative}
.abs{position:absolute}
section,header,footer{position:absolute;left:0;width:1200px}

/* header */
.site-header{top:0;height:73px;background:var(--white)}
.brand{left:160px;top:16px;display:flex;align-items:center;gap:10px}
.brand-dot{width:36px;height:36px;border-radius:50%;background:var(--navy)}
.brand-name{font-weight:600;font-size:17px;color:var(--navy);line-height:1.05;width:90px}
.main-nav{left:349px;top:28px;display:flex;gap:38px;font-size:12px;font-weight:500;color:var(--ink);text-transform:uppercase}
.main-nav .caret{font-size:8px;margin-left:6px}
.header-phone{left:842px;top:22px;text-align:right;font-size:13px;color:var(--text);width:118px}
.header-phone b{color:var(--ink)}
.header-phone small{display:block;font-size:9px;color:var(--blue);font-weight:600}
.header-icons{left:996px;top:26px;display:flex;gap:20px}

/* hero */
.hero{top:73px;height:508px;background:radial-gradient(circle at 55% 45%,#8bc751 0%,#4c9f35 45%,#23702b 100%)}
.hero-kicker{left:250px;top:188px;color:var(--white);font-size:12px;font-weight:600}
.hero-title{left:250px;top:208px;color:var(--white);font-size:44px;font-weight:700;line-height:1}
.hero-lead{left:250px;top:312px;width:180px;color:var(--white);font-size:11px;line-height:1.6}
.hero-side{left:895px;top:185px;width:150px;color:var(--white);font-size:11px;line-height:1.55;text-align:center}
.hero-art{left:530px;top:40px;width:376px;height:468px;border-radius:6px;background:linear-gradient(180deg,rgba(40,40,40,.55),rgba(30,90,35,.75))}
.hero-arrow{top:240px;width:30px;height:30px;border:2px solid var(--white);border-radius:50%}
.hero-card{left:214px;top:382px;width:248px;height:136px;background:var(--white);box-shadow:0 8px 20px rgba(0,0,0,.15);padding:22px 38px}
.hero-card p{font-size:11px;color:var(--ink);line-height:1.6}
.btn{display:inline-flex;justify-content:space-between;align-items:center;width:132px;height:33px;border:3px solid var(--blue);font-size:11px;font-weight:500;color:var(--ink);padding:0 14px;background:var(--white)}
.btn.on-dark{background:transparent;color:var(--white)}
.hero-card .btn{margin-top:16px}

/* services */
.services{top:581px;height:220px}
.service{top:60px;width:248px;height:135px;border-bottom:1px solid #cfd6dc}
.service-icon{position:absolute;left:0;top:0;width:38px;height:38px}
.service h3{position:absolute;left:52px;top:4px;font-size:13px;font-weight:600;color:var(--ink);line-height:1.2}
.service p{position:absolute;left:0;top:54px;font-size:11px;line-height:1.6}
.details{position:absolute;font-size:11px;font-weight:600;color:var(--blue)}

/* intro */
.intro{top:801px;height:282px;text-align:center}
.section-title{font-size:21px;font-weight:700;color:var(--ink)}
.intro .section-title{position:absolute;left:0;width:1200px;top:60px}
.intro p{position:absolute;left:320px;width:560px;top:104px;font-size:12px;line-height:1.8}
.intro .btn{position:absolute;left:533px;top:194px}

/* capability */
.capability{top:1083px;height:703px;background:var(--grey-band)}
.capability .section-title{position:absolute;left:0;width:1200px;top:45px;text-align:center}
.cap-block{width:260px}
.cap-block h4{font-size:21px;font-weight:700;color:#4a4f55;padding-bottom:8px;border-bottom:1px solid #b9c0c8;margin-bottom:10px}
.cap-block ul{list-style:none}
.cap-block li{font-size:11px;color:var(--ink);line-height:1.5;padding-left:14px;position:relative}
.cap-block li::before{content:"";position:absolute;left:0;top:6px;width:5px;height:5px;background:var(--navy)}
.cap-symbol{left:485px;top:325px;width:236px;height:236px;border-radius:50%;background:radial-gradient(circle,#9fd35a 0%,#5fae33 55%,rgba(95,174,51,0) 72%)}
.capability .btn{position:absolute;left:533px;top:619px}

/* posts */
.posts{top:1786px;height:369px}
.post{top:70px;width:248px}
.post-img{height:133px;position:relative}
.post-tag{position:absolute;left:8px;bottom:10px;background:#4a4a4a;color:var(--white);font-size:9px;padding:3px 10px}
.post p{font-size:11px;margin-top:18px;padding-bottom:10px;border-bottom:1px solid #d5dadf}
.post .details{position:static;display:block;margin-top:10px}
.subscribe{left:475px;top:70px;width:248px;height:133px;background:#8a8a8a;text-align:center;padding-top:28px}
.subscribe h5{color:var(--white);font-size:13px;font-weight:600;line-height:1.3}
.subscribe-form{display:flex;margin:16px auto 0;width:200px;height:34px}
.subscribe-form span{flex:1;background:var(--white);font-size:10px;text-align:left;padding:10px 12px;color:#555}
.subscribe-form i{width:34px;background:var(--blue);display:flex;align-items:center;justify-content:center}
.posts .btn{position:absolute;left:533px;top:278px}

/* bios */
.bios{top:2155px;height:422px;background:var(--grey-soft)}
.bio{top:77px;width:374px;height:272px;background:var(--white);box-shadow:0 4px 14px rgba(0,0,0,.08)}
.bio h3{position:absolute;left:22px;top:20px;font-size:21px;font-weight:400;color:var(--blue)}
.bio p{position:absolute;left:22px;top:58px;width:270px;font-size:9.5px;line-height:1.5;color:var(--ink)}
.bio svg{position:absolute;right:22px;top:28px}
.bio-img{position:absolute;left:0;top:106px;width:374px;height:166px}

/* case studies */
.cases{top:2577px;height:413px;background:var(--navy);text-align:center;color:var(--white)}
.cases .section-title{position:absolute;left:0;width:1200px;top:132px;color:var(--white)}
.cases p{position:absolute;left:320px;width:560px;top:178px;font-size:12px;line-height:1.8}
.cases .btn{position:absolute;left:533px;top:269px}

/* footer */
.site-footer{top:2990px;height:325px;background:var(--footer);color:var(--white)}
.footer-head{font-size:13px;font-weight:500;text-transform:uppercase;letter-spacing:.5px}
.map{left:161px;top:82px;width:226px;height:93px;background:linear-gradient(135deg,#e8ece4,#d6dfd0)}
.footer-address{left:161px;top:184px;font-size:10px;line-height:1.6;width:240px}
.footer-contact{left:161px;top:226px;font-size:10px;line-height:1.5}
.footer-contact div{display:flex;gap:8px;align-items:flex-start;margin-bottom:4px}
.sitemap ul{list-style:none;margin-top:16px}
.sitemap li{font-size:11px;line-height:26px}
.social-grid{left:712px;top:84px;display:grid;grid-template-columns:repeat(3,26px);gap:14px 12px}
.social-grid span{width:26px;height:26px;background:var(--white);opacity:.9}
.footer-brand{left:895px;top:40px;display:flex;align-items:center;gap:8px}
.footer-brand .brand-dot{width:32px;height:32px;background:var(--white)}
.footer-brand .brand-name{color:var(--white);font-size:15px}
.footer-copy{left:895px;top:118px;font-size:9.5px;line-height:1.5}
.footer-legal{left:895px;top:212px;font-size:9.5px}
</style>
</head>
<body>

<header class="site-header">
  <div class="abs brand"><span class="brand-dot"></span><span class="brand-name">Velno Recycling</span></div>
  <nav class="abs main-nav"><span>Home</span><span>Services<span class="caret">▼</span></span><span>About</span><span>Contact</span></nav>
  <div class="abs header-phone">(844)55-<b>VELNO</b> (83566)<small>TOLL FREE</small></div>
  <div class="abs header-icons">
    <svg width="16" height="16" viewBox="0 0 16 16"><circle cx="6.5" cy="6.5" r="5" fill="none" stroke="#222a33" stroke-width="2"/><line x1="10.5" y1="10.5" x2="15" y2="15" stroke="#222a33" stroke-width="2"/></svg>
    <svg width="16" height="16" viewBox="0 0 16 16"><rect y="2" width="16" height="2" fill="#222a33"/><rect y="7" width="16" height="2" fill="#222a33"/><rect y="12" width="16" height="2" fill="#222a33"/></svg>
  </div>
</header>

<section class="hero">
  <div class="abs hero-art" role="img" aria-label="Green recycling bin overflowing with old computers, towers and circuit boards"></div>
  <p class="abs hero-kicker">Electronic waste recycling</p>
  <h1 class="abs hero-title">ONE STOP<br>SHOP.</h1>
  <p class="abs hero-lead">Premier electronics recycling and remarketing companies in Austin, Texas.</p>
  <p class="abs hero-side">Electronic waste represents <b>2% of America's trash</b> in landfills, but it equals <b>70% of</b> overall toxic waste.</p>
  <span class="abs hero-arrow" style="left:30px"><svg width="26" height="26" viewBox="0 0 26 26"><path d="M15 8l-5 5 5 5" fill="none" stroke="#fff" stroke-width="2"/></svg></span>
  <span class="abs hero-arrow" style="left:1138px"><svg width="26" height="26" viewBox="0 0 26 26"><path d="M11 8l5 5-5 5" fill="none" stroke="#fff" stroke-width="2"/></svg></span>
  <div class="abs hero-card">
    <p>Providing a full "<b>chain of custody</b>" on electronic waste recycling.</p>
    <span class="btn">How it Works <span>›</span></span>
  </div>
</section>

<section class="services">
  <div class="abs service" style="left:214px">
    <svg class="service-icon" viewBox="0 0 38 38"><circle cx="19" cy="19" r="17" fill="none" stroke="#3f9a35" stroke-width="5" stroke-dasharray="24 4"/></svg>
    <h3>eWaste<br>Recycling</h3>
    <p>Electronic waste recycling and electronics remarketing program for customers.</p>
    <span class="details" style="left:0;top:114px">Details ›</span>
  </div>
  <div class="abs service" style="left:475px">
    <svg class="service-icon" viewBox="0 0 38 38"><path d="M6 2h18l8 8v26H6z" fill="#1a73c9"/><path d="M24 2v8h8" fill="#6fb0ea"/></svg>
    <h3>Data<br>Destruction</h3>
    <p>Data Destruction with our state of the art Degaussing equipment.</p>
    <span class="details" style="left:0;top:114px">Details ›</span>
  </div>
  <div class="abs service" style="left:738px">
    <svg class="service-icon" viewBox="0 0 38 38"><path d="M19 2l15 6v10c0 9-7 16-15 18C11 34 4 27 4 18V8z" fill="#1a73c9"/><path d="M11 18l6 6 11-12" fill="none" stroke="#fff" stroke-width="3.5"/></svg>
    <h3>Global Logistics<br>Support</h3>
    <p>Care about keeping our clients recycle and remarketing equipment safe.</p>
    <span class="details" style="left:0;top:114px">Details ›</span>
  </div>
</section>

<section class="intro">
  <h2 class="section-title">Velno Recycling</h2>
  <p>We started Velno Recycling in 2006 to fill the void as a full service computer and electronic waste recycling "one stop shop." Since our inception over ten years ago, we've become one of the premier electronics recycling and remarketing companies in Austin, Texas.</p>
  <span class="btn">Learn More <span>›</span></span>
</section>

<section class="capability">
  <h2 class="section-title">Capability Overview</h2>
  <div class="abs cap-block" style="left:499px;top:128px">
    <h4>RECYCLING</h4>
    <ul><li>Certified Global Recycling Capabilities</li><li>Sort by commodity</li><li>Certificate of Recycling</li><li>Data Destruction</li><li>Verifiable Certified Downstream Vendors</li></ul>
  </div>
  <div class="abs cap-block" style="left:214px;top:275px">
    <h4>LOGISTICS</h4>
    <ul><li>Global Logistics Support</li><li>Global Warehouse Capabilities</li><li>Global Audit Capabilities</li><li>Inventory Management</li><li>Asset Management</li><li>Bill of Lading</li><li>Proof of Delivery</li><li>Transfer of Ownership (TOO)</li></ul>
  </div>
  <div class="abs cap-block" style="left:796px;top:275px;width:200px">
    <h4>CERTIFICATES</h4>
    <ul><li>R2 2013 Responsible Recycling Certified</li><li>ISO 14001:2015</li><li>OHSAS 18001:2007</li><li>State Environmental Quality Registry (SEQR)</li><li>Regulated Entity # RN104829317</li><li>GDPR Compliant</li><li>HIPPA Compliant</li></ul>
  </div>
  <div class="abs cap-symbol" role="img" aria-label="Large green recycling arrows graphic"></div>
  <span class="btn">Learn More <span>›</span></span>
</section>

<section class="posts">
  <article class="abs post" style="left:214px">
    <div class="post-img" role="img" aria-label="Desk with a computer monitor, keyboard and phone" style="background:linear-gradient(135deg,#dfe8f0,#8aa3b8)"><span class="post-tag">Recycle Computer</span></div>
    <p>electronic waste recycling "one stop shop.</p>
    <span class="details">Details ›</span>
  </article>
  <div class="abs subscribe">
    <h5>Subscribe to keep<br>up to date</h5>
    <div class="subscribe-form"><span>Enter Email</span><i><svg width="14" height="10" viewBox="0 0 14 10"><rect x=".5" y=".5" width="13" height="9" fill="none" stroke="#fff"/><path d="M1 1l6 5 6-5" fill="none" stroke="#fff"/></svg></i></div>
  </div>
  <article class="abs post" style="left:475px;top:215px">
    <p style="margin-top:6px">electronic waste recycling "one stop shop.</p>
  </article>
  <article class="abs post" style="left:738px">
    <div class="post-img" role="img" aria-label="Hand holding a camera lens" style="background:linear-gradient(135deg,#d9d4cf,#2b2b2b)"><span class="post-tag">Recycle Camera</span></div>
    <p>electronic waste recycling "one stop shop.</p>
    <span class="details">Details ›</span>
  </article>
  <span class="btn">View All <span>›</span></span>
</section>

<section class="bios">
  <article class="abs bio" style="left:214px">
    <h3>Company Bio</h3>
    <p>That is one of the reasons we started Velno Recycling in 2006 to fill the void as a full service computer and c" Since</p>
    <svg width="20" height="14" viewBox="0 0 20 14"><path d="M0 7h18M12 1l6 6-6 6" fill="none" stroke="#1ba1e2" stroke-width="1.5"/></svg>
    <div class="bio-img" role="img" aria-label="Tweezers placing components on a green circuit board" style="background:linear-gradient(135deg,#e6e6e2,#2e6b4a)"></div>
  </article>
  <article class="abs bio" style="left:612px">
    <h3>Dale Corwin (CEO) Bio</h3>
    <p>That is one of the reasons we started Velno Recycling in 2006 to fill the void as a full service computer and c" Since</p>
    <svg width="20" height="14" viewBox="0 0 20 14"><path d="M0 7h18M12 1l6 6-6 6" fill="none" stroke="#1ba1e2" stroke-width="1.5"/></svg>
    <div class="bio-img" role="img" aria-label="Hands dismantling a computer power supply unit" style="background:linear-gradient(135deg,#c9a26b,#cfcac2)"></div>
  </article>
</section>

<section class="cases">
  <h2 class="section-title">Case Studies</h2>
  <p>We started Velno Recycling in 2006 to fill the void as a full service computer and electronic waste recycling "one stop shop." Since our inception over ten years ago, we've become one of the premier electronics recycling and remarketing companies in Austin, Texas.</p>
  <span class="btn on-dark">Learn More <span>›</span></span>
</section>

<footer class="site-footer">
  <h6 class="abs footer-head" style="left:161px;top:52px">Location</h6>
  <div class="abs map" role="img" aria-label="Street map showing the office location"></div>
  <p class="abs footer-address">4120 Marlow Ridge Blvd Austin,<br>Texas 78790</p>
  <div class="abs footer-contact">
    <div><svg width="10" height="10" viewBox="0 0 10 10"><path d="M2 1l2 2-1 1.5c.7 1.3 1.2 1.8 2.5 2.5L7 6l2 2-1.5 1.5C4.5 9 1 5.5.5 2.5z" fill="#fff"/></svg><span>(512)555-0142<br>(512)555-0187<br>(844)55-VELNO (83566) Toll Free</span></div>
    <div><svg width="10" height="8" viewBox="0 0 10 8"><rect x=".5" y=".5" width="9" height="7" fill="none" stroke="#fff"/><path d="M1 1l4 3 4-3" fill="none" stroke="#fff"/></svg><span>Dale@VelnoRecycling.com</span></div>
  </div>
  <div class="abs sitemap" style="left:462px;top:52px">
    <h6 class="footer-head">Sitemap</h6>
    <ul><li>Home</li><li>Services</li><li>About</li><li>Case Studies</li><li>Projects</li><li>Contact</li></ul>
  </div>
  <h6 class="abs footer-head" style="left:712px;top:52px">Social</h6>
  <div class="abs social-grid"><span></span><span></span><span></span><span></span><span></span></div>
  <div class="abs footer-brand"><span class="brand-dot"></span><span class="brand-name">Velno Recycling</span></div>
  <p class="abs footer-copy">© 2018 VelnoRecycling.com<br>All Rights Reserved</p>
  <p class="abs footer-legal">Privacy | Legal | T&amp;C | Cookies</p>
</footer>

</body>
</html>
```